Integrative Medical Practice Website Redo

I am needing to have our current website redesigned to make it a responsive website to work on smartphones.
Current website
www.brightoakfm.com
Here are several examples of what I am looking for
https://www.corvanhealth.com/
I am wanting a popup for a newsletter signup
Looking for a very professional, clean, simple, minimalist, bold well designed website
Colors would ideally be greens and blues, cool tones, muted colors, or graytones like:
https://journeybright.org/
Several other clean design examples
http://7harborsrenton.com/
http://www.belvomedical.com/
http://sunpathyouth.com/
http://yourcellduke.com/
I would like the top navigation bar to be able to slide down while browsing site
We are also needing to add several features that are not on our current website:
Questionnaire buttons
Are you toxic questionnaire?
Take our hormone quiz to find out if hormones are affecting your health.
online scheduling option for:
nutrition counselling
testing like body composition, basal metabolic rate, CIMT, breast thermography, VO2 Max testing, Vita Trace
Therapies like whole body vibration, infrared sauna, Exercise with oxygen, hyperbaric oxygen, spinal decompression
Need to have separate page for different services and split up services into:
Consults/Office Visits, Testing, Therapies, Procedures
Need to have a button link to patient portal
Needs to have online store
Need to add navigation button "Start Here"
Need a spot for a video on practice summary
Newsletter signup to collect emails
Testimonials from linkpage
Blog that posts can be shared with social media
Password protected patient access that can integrate into crate.net ideally
Modules for programs online classes/videos
I have attached stock images that you can use, but feel free to find others to use.
I have also attached a copy of our current brochure that shows an overview of the practice
Target Market(s)
Health conscious people of all ages looking for a family medicine doctor
Industry/Entity Type
Alternative Medicine
Coding
Coded - Design and coding required
Number of Pages Required
5+ page
Look and feel

```html
<!DOCTYPE html>
<html lang="en">
<head>
<meta charset="utf-8">
<title>Bright Oak Family Medicine</title>
<link rel="stylesheet" href="https://fonts.googleapis.com/css2?family=Roboto:ital,wght@0,400;0,500;0,700;1,400&display=swap">
<style>
:root{
  --blue-dark:#2a6f93;
  --blue:#3b8db5;
  --blue-light:#5bb2d1;
  --green:#5e9e2f;
  --ink:#2b2b2b;
  --muted:#555;
  --paper:#f4f5f7;
  --white:#fff;
}
*{box-sizing:border-box;margin:0;padding:0}
html,body{width:678px;height:1200px;overflow:hidden}
body{font-family:"Roboto",Arial,sans-serif;color:var(--ink);background:var(--white);position:relative}
.abs{position:absolute}

/* hero */
.hero{left:0;top:0;width:678px;height:308px;background:linear-gradient(180deg,#aec3d3 0%,#c3d2dc 55%,#a3b9a4 80%,#8ea56a 100%)}
.hero-hands{left:380px;top:70px;width:298px;height:238px;background:linear-gradient(160deg,rgba(120,150,80,.0) 0%,rgba(190,160,135,.55) 45%,rgba(160,130,105,.7) 100%)}
.hero-sheen{left:0;top:0;width:678px;height:308px;background:linear-gradient(115deg,rgba(255,255,255,.32) 0%,rgba(255,255,255,.22) 48%,rgba(255,255,255,0) 48.2%)}
.topbar{left:0;top:0;width:678px;height:38px;border-bottom:1px solid rgba(255,255,255,.35)}
.brand{left:28px;top:7px;display:flex;align-items:center;gap:6px;color:var(--white)}
.brand-dot{width:10px;height:10px;border-radius:50%;background:var(--white)}
.brand-name{font-size:15px;font-weight:500;line-height:1}
.nav{left:203px;top:15px;display:flex;gap:21px}
.nav a{color:var(--white);font-size:9px;font-weight:500;text-decoration:none;letter-spacing:.2px}
.btn-pill{top:10px;height:19px;border-radius:10px;font-size:7.5px;line-height:17px;text-align:center}
.btn-login{left:559px;width:35px;border:1px solid var(--white);color:var(--white)}
.btn-new{left:597px;width:55px;background:var(--white);color:var(--ink);border:1px solid var(--white)}

/* welcome */
.welcome{left:0;top:308px;width:678px;height:62px;background:linear-gradient(90deg,var(--blue-dark),var(--blue-light));color:var(--white);text-align:center}
.welcome h1{font-size:12.5px;font-weight:700;margin-top:3px}
.welcome hr{border:0;border-top:1px dashed rgba(255,255,255,.75);width:620px;margin:6px auto 0}
.welcome p{font-size:7px;line-height:11px;width:630px;margin:7px auto 0}

/* section titles */
.section-title{left:0;width:678px;text-align:center;font-size:12px;font-weight:700;color:var(--ink)}
.section-title span{color:var(--green)}
.dash{left:29px;width:620px;border-top:1px dashed #8a9b70}

/* services */
.services{left:0;top:370px;width:678px;height:172px;background:var(--paper)}
.card{top:435px;width:143px;height:70px}
.card-label{top:494px;width:131px;height:23px;background:linear-gradient(180deg,#3f92b8,var(--blue-dark));color:var(--white);font-size:9.5px;font-weight:500;text-align:center;line-height:23px;border-radius:2px}
.card-icon{top:421px;width:28px;height:28px;border-radius:50%;background:var(--blue-dark);border:2px solid var(--white);display:flex;align-items:center;justify-content:center}

/* mail + video */
.mail{left:0;top:542px;width:339px;height:200px;background:linear-gradient(135deg,var(--blue-dark),var(--blue-light))}
.mail h2{position:absolute;left:0;top:12px;width:339px;text-align:center;color:var(--white);font-size:15px;font-weight:500}
.field{background:var(--white);border:1px solid #cfd8de;border-radius:2px;height:18px;font-size:7px;color:#888;padding:5px 8px;line-height:8px}
.send{left:131px;top:707px;width:77px;height:18px;background:var(--white);border-radius:2px;font-size:7.5px;font-weight:500;text-align:center;line-height:18px;color:var(--ink)}
.video{left:339px;top:542px;width:339px;height:200px;background:linear-gradient(90deg,#7d7a5a 0%,#b8a98c 35%,#c4a58c 60%,#a8957e 80%,#8a8a7e 100%)}
.play{left:490px;top:622px;width:54px;height:38px;border-radius:9px;background:#d9302a;display:flex;align-items:center;justify-content:center}

/* testimonials */
.quote{font-size:7px;font-style:italic;line-height:11px;color:var(--muted)}
.who{font-size:7px;color:var(--ink);margin-top:6px;font-style:normal}
.avatar{width:44px;height:44px;border-radius:50%;background:#b9a596}
.rule-v{left:339px;top:805px;height:125px;border-left:1px dashed #8a9b70}

/* like bar */
.likebar{left:0;top:942px;width:678px;height:36px;background:#eef0f2}
.like-pill{left:212px;top:946px;width:254px;height:27px;background:var(--white);border:1px solid #dde1e5;border-radius:14px}
.like-btn{left:280px;top:953px;width:27px;height:10px;background:#3b6fc9;border-radius:2px;color:var(--white);font-size:5.5px;line-height:10px;text-align:center;font-weight:700}
.like-text{left:310px;top:954px;font-size:5.5px;color:#444}

/* footer */
.footer{left:0;top:978px;width:678px;height:222px;background:linear-gradient(135deg,var(--blue-dark),var(--blue-light))}
.col{color:var(--white)}
.col h3{font-size:10px;font-weight:700}
.col p{font-size:7px;line-height:11px}
.map{left:188px;top:1010px;width:280px;height:111px;background:linear-gradient(90deg,#dfe3d6 0%,#d7e2d8 30%,#9ec7e2 45%,#a9cde4 70%,#e6e3d8 100%)}
.social{left:29px;top:1113px;display:flex;gap:8px}
.social i{display:block;width:8px;height:8px;border-radius:50%;background:var(--white)}
.email-box{left:506px;top:1101px;width:143px;height:18px;background:var(--white);border-radius:9px;font-size:7px;color:var(--ink);padding-left:9px;line-height:18px}
.go{left:618px;top:1101px;width:31px;height:18px;background:var(--green);border-radius:9px;font-size:7px;color:var(--white);text-align:center;line-height:18px}
.foot-rule{left:29px;top:1162px;width:620px;border-top:1px solid rgba(255,255,255,.5)}
.foot-small{top:1178px;font-size:6.5px;font-weight:700;color:var(--white)}
</style>
</head>
<body>

<div class="abs hero" role="img" aria-label="Hero photo of cupped hands holding a small bonsai tree over a soft landscape"></div>
<div class="abs hero-hands"></div>
<div class="abs hero-sheen"></div>

<header class="abs topbar">
  <div class="abs brand"><span class="brand-dot"></span><span class="brand-name">Bright Oak</span></div>
  <nav class="abs nav"><a>HOME</a><a>ABOUT</a><a>SERVICES</a><a>RESOURCES</a><a>CONTACT</a></nav>
  <div class="abs btn-pill btn-login">Log In</div>
  <div class="abs btn-pill btn-new">New Patient</div>
</header>

<section class="abs welcome">
  <h1>Welcome to Bright Oak Family Medicine</h1>
  <hr>
  <p>We provide innovative, quality family health care by uniquely combining both conventional and alternative medicine. This "best of both worlds" approach provides patients with options in the management of their concerns while addressing the root cause.</p>
</section>

<section class="abs services"></section>
<h2 class="abs section-title" style="top:381px">Our <span>Services</span></h2>
<div class="abs dash" style="top:402px"></div>

<div class="abs card" style="left:29px;background:linear-gradient(180deg,#efe2d8,#e2c2ad)" role="img" aria-label="Photo of a relaxing massage"></div>
<div class="abs card" style="left:188px;background:linear-gradient(180deg,#e3e8ee,#7d8793)" role="img" aria-label="Photo of treadmill fitness testing"></div>
<div class="abs card" style="left:346px;background:linear-gradient(180deg,#b9cbeb,#eee8d8)" role="img" aria-label="Photo of a daisy held in hands"></div>
<div class="abs card" style="left:505px;background:linear-gradient(180deg,#f2efec,#cdc6bf)" role="img" aria-label="Photo of a person filling in a form"></div>

<div class="abs card-icon" style="left:87px"><svg width="12" height="12" viewBox="0 0 12 12"><rect x="4" y="1" width="4" height="2" fill="#fff"/><rect x="3" y="3" width="6" height="8" rx="1" fill="#fff"/></svg></div>
<div class="abs card-icon" style="left:245px"><svg width="12" height="12" viewBox="0 0 12 12"><path d="M3 1v4L1 10h5L4 5V1z" fill="#fff"/><circle cx="9" cy="8" r="2.5" fill="#fff"/></svg></div>
<div class="abs card-icon" style="left:404px"><svg width="12" height="12" viewBox="0 0 12 12"><circle cx="6" cy="3" r="2" fill="#fff"/><rect x="1" y="7" width="10" height="3" rx="1" fill="#fff"/></svg></div>
<div class="abs card-icon" style="left:562px"><svg width="12" height="12" viewBox="0 0 12 12"><rect x="2" y="1" width="8" height="10" rx="1" fill="none" stroke="#fff"/><path d="M4 4h4M4 6h4M4 8h3" stroke="#fff"/></svg></div>

<div class="abs card-label" style="left:35px">Modalities</div>
<div class="abs card-label" style="left:194px">Testing</div>
<div class="abs card-label" style="left:352px">Therapies</div>
<div class="abs card-label" style="left:511px">Questionnaire</div>

<section class="abs mail"><h2>Feel Free to Mail</h2></section>
<div class="abs field" style="left:28px;top:585px;width:136px">Name *</div>
<div class="abs field" style="left:175px;top:585px;width:136px">Email *</div>
<div class="abs field" style="left:28px;top:614px;width:136px">Phone Number</div>
<div class="abs field" style="left:175px;top:614px;width:136px">Subject</div>
<div class="abs field" style="left:28px;top:643px;width:283px;height:52px">Write Your Message Here...</div>
<div class="abs send">SEND MESSAGE</div>
<div class="abs video" role="img" aria-label="Practice summary video showing a patient during a VO2 max test"></div>
<div class="abs play"><svg width="16" height="16" viewBox="0 0 16 16"><path d="M3 1.5L14 8 3 14.5z" fill="#fff"/></svg></div>

<h2 class="abs section-title" style="top:751px">What <span>People Say</span></h2>
<div class="abs dash" style="top:772px"></div>

<div class="abs quote" style="left:29px;top:805px;width:232px;text-align:right">At vero eos et accusamus et iusto odio dignissimos ducimus qui blanditiis praesentium voluptatum deleniti atque corrupti quos dolores et quas molestias excepturi sint occaecati.<div class="who">Owen Marsh , Developer</div></div>
<div class="abs avatar" style="left:277px;top:805px" role="img" aria-label="Portrait of client"></div>
<div class="abs avatar" style="left:357px;top:805px" role="img" aria-label="Portrait of client"></div>
<div class="abs quote" style="left:417px;top:805px;width:232px">Luis aute irure dolor in reprehenderit in piluptate velit esse cillum dolore eu fugiat nulla pariatur. Excepteur sint occaecat cupidatat non proident, sunt in culpa qui officia deserunt mollit.<div class="who">Nora Vale , Manager</div></div>

<div class="abs dash" style="top:867px"></div>
<div class="abs rule-v"></div>

<div class="abs quote" style="left:29px;top:883px;width:232px;text-align:right">Provident, similique sunt in culpa qui officia deserunt mollitia animi, id est laborum et dolorum fuga. Et harum quidem rerum facilis est et expedita distinctio. Nam libero tempore, cum soluta nobis.<div class="who">Irene Cole , Creative Designer</div></div>
<div class="abs avatar" style="left:277px;top:883px" role="img" aria-label="Portrait of client"></div>
<div class="abs avatar" style="left:357px;top:883px" role="img" aria-label="Portrait of client"></div>
<div class="abs quote" style="left:417px;top:883px;width:232px">Duis aute irure dolor in reprehenderit in voluptate velit esse cillum dolore eu fugiat nulla pariatur. Excepteur sint occaecat cupidatat non proident, sunt in culpa qui officia deserunt mollit.<div class="who">Paul Reyes , Operations Manager</div></div>

<div class="abs likebar"></div>
<div class="abs like-pill"></div>
<div class="abs" style="left:245px;top:946px;width:1px;height:27px;background:#dde1e5"></div>
<div class="abs" style="left:224px;top:953px"><svg width="11" height="11" viewBox="0 0 11 11"><rect x="0.5" y="4.5" width="2" height="6" fill="none" stroke="#bbb"/><path d="M3.5 10.5V4.5L6 0.8c1 0 1.2.8 1 1.7L6.6 4.2H10c.6 0 .9.6.7 1.1l-1.4 4.6c-.1.4-.5.6-.9.6z" fill="none" stroke="#bbb"/></svg></div>
<div class="abs like-btn">Like</div>
<div class="abs like-text">You and 4k others like this.</div>

<footer class="abs footer"></footer>
<div class="abs col" style="left:29px;top:988px;width:160px">
  <h3>Contact Us</h3>
  <p style="margin-top:9px;width:145px">Please feel free to contact us for any issue. Our staff is available to you from 9AM until 5PM on weekdays.</p>
  <p style="margin-top:8px"><b>Phone:</b> +1 (555) 210 48 73</p>
  <p style="margin-top:8px"><b>Office:</b> 410 Oak Circle, Fairmont, TX 79000</p>
  <p style="margin-top:8px"><b>Email:</b> info@brightoakfm.com</p>
</div>
<div class="abs social"><i></i><i></i><i></i><i></i><i></i></div>

<h3 class="abs" style="left:188px;top:988px;width:280px;text-align:center;color:#fff;font-size:10px;font-weight:700">Headquarters</h3>
<div class="abs map" role="img" aria-label="Street map showing the office location"></div>

<div class="abs col" style="left:506px;top:988px;width:145px">
  <h3>Newsletter Signup</h3>
  <p style="margin-top:9px">Temporibus autem quibusdam et aut officiis debitis aut rerum necessitatibus saepe eveniet ut et voluptates repudian.</p>
  <p style="margin-top:11px">Temporibus autem quibusdam et aut officiis debitis aut rerum necessitatibus saepe eveniet ut et voluptates repudian.</p>
</div>
<div class="abs email-box">Email address</div>
<div class="abs go">GO</div>

<div class="abs foot-rule"></div>
<div class="abs foot-small" style="left:29px">Copyright © Bright Oak Family Medicine</div>
<div class="abs" style="left:304px;top:1172px;display:flex;align-items:center;gap:5px;color:#fff"><span style="width:8px;height:8px;border-radius:50%;background:#fff;display:block"></span><span style="font-size:12px;font-weight:500">Bright Oak</span></div>
<div class="abs foot-small" style="left:593px">All rights reserved</div>

</body>
</html>
```